Website for Torvane Capital - investment banking firm

We have a corporate identity (thanks to Ravella/48213) and want to extend that into a website design.  See the attached zipped files.
We have software folks in-house to do the coding.
See the attached Project Brief & Notes for more details.  Don't worry about the actual text - lorem ipsum will be fine.
The server will be Apache.
Thank you!
Leopold

```html
<!DOCTYPE html>
<html lang="en">
<head>
<meta charset="utf-8">
<title>Torvane Capital</title>
<link href="https://fonts.googleapis.com/css2?family=Open+Sans:ital,wght@0,300;0,400;0,600;0,700;1,400;1,600&family=Lora:ital@1&family=Shadows+Into+Light&display=swap" rel="stylesheet">
<style>
:root{
  --brand:#1f4f9c;
  --ink:#333;
  --muted:#8a8a8a;
  --line:#e3e3e3;
  --page:#e6e6e6;
  --band:#efefef;
  --footer:#1e1e1e;
  --footer-deep:#141414;
  --white:#fff;
}
*{box-sizing:border-box;margin:0;padding:0}
html,body{width:1200px;height:2516px;overflow:hidden}
body{background:var(--page);font-family:"Open Sans",Arial,sans-serif;color:var(--ink);font-size:13px;position:relative}
.site{position:absolute;left:146px;top:0;width:910px;height:2500px;background:var(--white);border-top:5px solid var(--brand);overflow:hidden}
.site>*{position:relative;overflow:hidden}
.abs{position:absolute}

/* header */
.header{height:106px}
.logo{left:24px;top:40px;display:flex;align-items:center;gap:10px}
.logo-mark{width:32px;height:32px;background:var(--brand);border-radius:3px}
.logo-name{font-size:24px;font-weight:600;color:var(--brand);letter-spacing:.3px}
.topbar{right:30px;top:26px;display:flex;align-items:center;gap:14px;font-size:10px;color:var(--muted)}
.search{width:120px;height:22px;border:1px solid #ccc;border-radius:11px;padding:4px 10px;font-size:10px;color:#aaa}
.nav{right:30px;top:62px;display:flex;align-items:center;gap:4px}
.nav a{font-size:10px;font-weight:700;color:var(--brand);text-decoration:none;padding:7px 9px;border-radius:3px}
.nav a.active{background:var(--brand);color:var(--white)}
.social{display:flex;gap:5px;margin-left:12px}
.social span{width:20px;height:20px;border-radius:50%;border:1px solid #ccc;display:block}

/* hero */
.hero{height:460px}
.hero-visual{height:372px;background:
  radial-gradient(ellipse 260px 180px at 72% 62%,rgba(214,190,60,.55),rgba(214,190,60,0) 70%),
  radial-gradient(ellipse 200px 240px at 28% 40%,rgba(150,150,155,.7),rgba(150,150,155,0) 70%),
  linear-gradient(180deg,#2c2e33 0%,#454850 55%,#1d1e22 100%)}
.hero-caption{height:88px;background:#1c1d20;color:var(--white);padding:20px 24px;position:relative}
.hero-caption h2{font-size:14px;font-weight:400}
.hero-caption h2 em{font-family:"Shadows Into Light",cursive;font-style:normal;font-size:21px;margin-left:4px}
.hero-caption p{font-size:10px;color:#aaa;margin-top:2px}
.btn{position:absolute;right:110px;top:26px;background:var(--brand);color:var(--white);font-size:12px;font-weight:600;padding:8px 14px;border-radius:3px}
.learn{position:absolute;right:30px;top:34px;font-size:10px;color:#999}

/* intro */
.intro{height:189px;text-align:center;padding-top:48px}
.intro h1{font-size:26px;font-weight:300;color:#444}
.intro h1 mark{background:var(--brand);color:var(--white);font-weight:600;padding:2px 8px}
.intro p{font-size:14px;color:#b5b5b5;width:820px;margin:18px auto 0;line-height:1.6}

/* process */
.process{height:360px}
.step{position:absolute;top:81px;width:124px;text-align:center}
.step-ring{width:124px;height:124px;border-radius:50%;border:2px dashed #cfcfcf;display:flex;align-items:center;justify-content:center;background:var(--white)}
.step-core{width:104px;height:104px;border-radius:50%;background:#f3f3f3;display:flex;align-items:center;justify-content:center}
.step-label{font-family:"Lora",Georgia,serif;font-style:italic;font-size:18px;color:#666;margin-top:20px}
.work{position:absolute;left:590px;top:2px;width:266px;height:266px;border-radius:50%;border:2px dashed #ccc;overflow:hidden;background:var(--white)}
.work-photo{position:absolute;left:32px;top:40px;width:200px;height:108px;background:linear-gradient(135deg,#c9ccd1,#6f747c)}
.work-tag{position:absolute;left:62px;top:58px;font-size:10px;color:var(--white);font-weight:600}
.work-brands{position:absolute;left:42px;top:166px;display:flex;gap:10px}
.work-brands span{width:28px;height:10px;background:#d6d6d6;border-radius:2px}
.work-note{position:absolute;left:52px;top:196px;font-size:8px;color:#888}
.work-label{position:absolute;left:668px;top:296px;width:110px;text-align:center;font-family:"Lora",Georgia,serif;font-style:italic;font-size:18px;color:#666}

/* features */
.features{height:330px}
.features h3,.sidebar h3{font-size:25px;font-weight:300;color:#333}
.features>h3{position:absolute;left:24px;top:16px}
.features h3 b,.band h3 b{font-weight:700}
.feature-grid{position:absolute;left:24px;top:78px;width:540px;display:grid;grid-template-columns:296px 244px;row-gap:24px}
.feature{display:flex;gap:12px;height:30px}
.feature i{width:22px;height:22px;border-radius:50%;background:var(--brand);flex:none}
.feature h4{font-size:12px;font-weight:400;color:var(--brand);line-height:1.3}
.feature p{font-size:9.5px;color:#888;margin-top:2px}
.sidebar{position:absolute;left:614px;top:16px;width:272px}
.acc{margin-top:20px;border:1px solid var(--line)}
.acc div{font-size:10.5px;color:var(--brand);padding:10px 12px;border-bottom:1px solid var(--line);background:#f6f6f6}
.acc div:last-child{border-bottom:0}
.acc p{font-size:9.5px;color:#888;padding:10px 12px;border-bottom:1px solid var(--line);line-height:1.5}

/* clients */
.clients{height:260px;text-align:center;padding-top:30px}
.clients h3{font-size:25px;font-weight:300;color:#333}
.clients h3 b{font-weight:700}
.clients .sub{font-size:13px;color:var(--brand);margin-top:8px}
.brand-row{display:flex;justify-content:space-between;align-items:center;padding:0 110px 0 120px;margin-top:40px}
.brand-row span{font-size:21px;font-weight:600;color:#555}
.dots{display:flex;gap:7px;justify-content:center;margin-top:22px}
.dots i{width:7px;height:7px;border-radius:50%;background:#ccc}
.dots i.on{background:#888}

/* collage */
.collage-wrap{height:126px;padding:12px 100px 0}
.collage{height:114px;border-radius:40px 60px 0 0;background:linear-gradient(90deg,#9a8f7c 0%,#6f7d8c 22%,#b19a78 40%,#d8d3ca 50%,#8c7f6a 62%,#5f6e80 80%,#a8947a 100%)}

/* band */
.band{height:349px;background:var(--band)}
.blog{position:absolute;left:24px;top:34px;width:430px}
.band h3{font-size:24px;font-weight:300;color:#333}
.posts{display:flex;gap:20px;margin-top:22px}
.post{width:210px;display:flex;gap:8px}
.date{width:30px;flex:none;text-align:center}
.date b{display:block;background:var(--white);font-size:12px;padding:4px 0}
.date span{display:block;background:var(--brand);color:var(--white);font-size:8px;padding:2px 0}
.post h4{font-size:12.5px;font-weight:400;color:var(--brand);line-height:1.35}
.post p{font-size:9.5px;color:#888;margin-top:8px;line-height:1.6}
.post p em{color:var(--brand);font-style:normal}
.testimonials{position:absolute;left:464px;top:34px;width:422px}
.quote{margin-top:18px;background:var(--brand);color:var(--white);font-style:italic;font-weight:600;font-size:11.5px;line-height:1.45;padding:14px 26px 14px 30px;border-radius:4px;position:relative}
.quote:after{content:"";position:absolute;left:28px;bottom:-10px;border:10px solid transparent;border-top-color:var(--brand);border-bottom:0}
.author{display:flex;gap:12px;margin-top:20px;align-items:center}
.avatar{width:44px;height:44px;background:#9ea4ad}
.author b{font-size:12px;display:block}
.author span{font-size:9px;color:#888}
.band .dots{position:absolute;margin:0}

/* footer */
.footer{height:245px;background:var(--footer);color:#999;overflow:visible}
.touch{position:absolute;left:26px;top:-10px;background:var(--brand);color:var(--white);font-family:"Shadows Into Light",cursive;font-size:15px;padding:2px 16px;transform:skewX(-8deg)}
.fcol{position:absolute;top:64px}
.fcol h5{font-size:15px;font-weight:400;color:#ddd;margin-bottom:12px}
.fcol p{font-size:9px;line-height:1.7;color:#777}
.field{display:flex;margin-top:18px}
.field span{width:168px;height:24px;background:#eee;font-size:9px;color:#888;padding:6px 8px}
.field b{width:30px;height:24px;background:#ccc;color:#333;font-size:10px;font-weight:600;padding:5px 6px}
.contact li{list-style:none;font-size:9px;color:#888;margin-bottom:16px}
.fsocial{display:flex;gap:6px}
.fsocial span{width:22px;height:22px;border-radius:50%;background:var(--white)}
.copyright{height:70px;background:var(--footer-deep);font-size:9px;color:#666;padding:28px 24px}
</style>
</head>
<body>
<div class="site">
  <header class="header">
    <div class="abs logo"><span class="logo-mark"></span><span class="logo-name">Torvane Capital</span></div>
    <div class="abs topbar"><span>Contact Us</span><span>(123) 456-7890</span><span class="search">Search...</span></div>
    <nav class="abs nav">
      <a class="active">HOME</a><a>ABOUT US</a><a>SERVICES</a><a>CURRENT ENGAGEMENTS</a><a>COMPLETED TRANSACTIONS</a>
      <div class="social"><span></span><span></span><span></span></div>
    </nav>
  </header>

  <section class="hero">
    <div class="hero-visual" role="img" aria-label="Businessman sketching a rising bar chart on glass"></div>
    <div class="hero-caption">
      <h2>Lorem ipsum Lorem ipsum Lorem ipsum <em>Technology</em></h2>
      <p>Lorem ipsum Lorem ipsum</p>
      <span class="btn">Get Started Now!</span><span class="learn">or learn more</span>
    </div>
  </section>

  <section class="intro">
    <h1>Lorem <mark>Lorem ipsum</mark> Lorem ipsum Lorem ipsum Lorem ipsum</h1>
    <p>Lorem ipsum Lorem ipsum Lorem ipsum Lorem ipsum Lorem ipsum Lorem ipsumLorem ipsum Lorem ipsum Lorem ipsumLorem ipsum Lorem ipsum</p>
  </section>

  <section class="process">
    <svg class="abs" style="left:0;top:0" width="910" height="260" viewBox="0 0 910 260">
      <path d="M0 100 Q160 160 330 150 T590 130" fill="none" stroke="#cfcfcf" stroke-width="1.5" stroke-dasharray="4 4"/>
    </svg>
    <div class="step" style="left:98px">
      <div class="step-ring"><div class="step-core">
        <svg width="56" height="56" viewBox="0 0 56 56"><circle cx="28" cy="28" r="24" fill="none" stroke="#555" stroke-width="3"/><circle cx="28" cy="28" r="15" fill="none" stroke="#c0392b" stroke-width="4"/><circle cx="28" cy="28" r="6" fill="#555"/><path d="M28 28 L50 8" stroke="#333" stroke-width="3"/></svg>
      </div></div>
      <div class="step-label">Strategy</div>
    </div>
    <div class="step" style="left:247px">
      <div class="step-ring"><div class="step-core">
        <svg width="60" height="56" viewBox="0 0 60 56"><path d="M6 40 L54 24" stroke="#777" stroke-width="8" stroke-linecap="round"/><rect x="14" y="10" width="8" height="24" fill="#444"/><rect x="38" y="4" width="8" height="24" fill="#444"/></svg>
      </div></div>
      <div class="step-label">Planning</div>
    </div>
    <div class="step" style="left:393px">
      <div class="step-ring"><div class="step-core" style="background:#2e2e2e">
        <svg width="56" height="56" viewBox="0 0 56 56"><path d="M12 12 L44 44 M44 12 L12 44" stroke="#fff" stroke-width="6" stroke-linecap="round"/></svg>
      </div></div>
      <div class="step-label">Strategy</div>
    </div>
    <div class="work">
      <div class="work-photo" role="img" aria-label="Business team meeting in an office"></div>
      <span class="work-tag">Lorem ipsum</span>
      <div class="work-brands"><span></span><span></span><span></span><span></span><span></span></div>
      <span class="work-note">Why Choose Us</span>
    </div>
    <div class="work-label">Our Work</div>
  </section>

  <section class="features">
    <h3>Our <b>Features</b></h3>
    <div class="feature-grid">
      <div class="feature"><i></i><div><h4>Lorem ipsum</h4><p>Lorem ipsum dolor sit amet, consectetur adip.</p></div></div>
      <div class="feature"><i></i><div><h4>Lorem ipsum</h4><p>Lorem ipsum dolor sit amet, consectetur.</p></div></div>
      <div class="feature"><i></i><div><h4>Lorem ipsum</h4><p>Lorem ipsum dolor sit amet, adip.</p></div></div>
      <div class="feature"><i></i><div><h4>Lorem ipsum</h4><p>Lorem ipsum dolor sit amet, consectetur adip.</p></div></div>
      <div class="feature"><i></i><div><h4>Lorem ipsum</h4><p>Lorem ipsum dolor sit amet, consectetur adip.</p></div></div>
      <div class="feature"><i></i><div><h4>Lorem ipsum</h4><p>Lorem ipsum dolor sit, consectetur adip.</p></div></div>
      <div class="feature"><i></i><div><h4>Lorem ipsum</h4><p>Lorem ipsum dolor sit amet, consectetur adip.</p></div></div>
      <div class="feature"><i></i><div><h4>Lorem ipsum</h4><p>Lorem ipsum dolor sit amet, consectetur adip.</p></div></div>
    </div>
    <aside class="sidebar">
      <h3>and more...</h3>
      <div class="acc">
        <div>Pricing Tables</div>
        <div>Contact Forms</div>
        <p>Donec tellus massa, tristique sit amet condimentum vel, facilisis quis sapien.</p>
        <div>Portfolio Pages</div>
      </div>
    </aside>
  </section>

  <section class="clients">
    <h3>Lorem ipsum Lorem ipsum <b>Lorem ipsum</b> Lorem ipsum</h3>
    <p class="sub">5,500 customers in 100 countries use Tessel Template. Meet our customers.</p>
    <div class="brand-row"><span>Quellon</span><span>Marlowe</span><span>Pennard</span><span>Ostrava</span><span>Calder</span><span>Pennard</span></div>
    <div class="dots"><i class="on"></i><i></i></div>
  </section>

  <div class="collage-wrap"><div class="collage" role="img" aria-label="World map made from a collage of photographs"></div></div>

  <section class="band">
    <div class="blog">
      <h3>Latest <b>Blog</b> Posts</h3>
      <div class="posts">
        <article class="post"><div class="date"><b>15</b><span>Jan</span></div><div><h4>Lorem ipsum dolor sit amet, consectetur adipiscing elit.</h4><p>Lorem ipsum dolor sit amet, consectetur adipiscing elit. Donec hendrerit vehicula est, in consequat libero. <em>read more »</em></p></div></article>
        <article class="post"><div class="date"><b>15</b><span>Jan</span></div><div><h4>Lorem ipsum dolor</h4><p>Lorem ipsum dolor sit amet, consectetur adipiscing elit. Donec hendrerit vehicula est. <em>read more »</em></p></div></article>
      </div>
    </div>
    <div class="dots" style="left:212px;top:270px"><i class="on"></i><i></i><i></i></div>
    <div class="testimonials">
      <h3><b>What</b> Client's Say</h3>
      <div class="quote">Lorem ipsum dolor sit amet, consectetur adipiscing elit. Donec hendrerit vehicula est, in consequat. Lorem ipsum dolor sit amet, consectetur adipiscing elit. Donec hendrerit vehicula est, in consequat. Donec hendrerit vehicula est, in consequat.</div>
      <div class="author"><div class="avatar" role="img" aria-label="Client portrait"></div><div><b>Lorem</b><span>CEO &amp; Founder - Other</span></div></div>
    </div>
    <div class="dots" style="left:664px;top:286px"><i class="on"></i><i></i></div>
  </section>

  <footer class="footer">
    <span class="touch">Get in Touch</span>
    <div class="fcol" style="left:24px;width:200px"><h5>Newsletter</h5><p>Lorem ipsum Lorem ipsum Lorem ipsum Lorem ipsum Lorem ipsum Lorem ipsum Lorem ipsum Lorem ipsum</p><div class="field"><span>Email Address</span><b>Go</b></div></div>
    <div class="fcol" style="left:245px;width:200px"><h5>Latest Tweet</h5><p>@loremipsum<br>Lorem ipsum dolor sit amet, consectetur adipiscing<br>19 mar<br><br>Lorem ipsum<br>22 mar</p></div>
    <div class="fcol" style="left:466px;width:260px"><h5>Contact Us</h5><ul class="contact"><li>Address: Lorem ipsum Lorem ipsum Lorem ipsum</li><li>Phone: (123) 456-7890</li><li>Email: mail@example.com</li></ul></div>
    <div class="fcol" style="left:764px"><h5>Follow Us</h5><div class="fsocial"><span></span><span></span><span></span></div></div>
  </footer>
  <div class="copyright">© Copyright 2014. All Rights Reserved.</div>
</div>
</body>
</html>
```